"Made in Chicago" Baby Shower Invitation

I need a design for a baby shower invitation with the headline and theme of "Made in Chicago". The design should incorporate the colors/design of the Chicago flag. I have attached an image of the flag for your reference. The design should be sized 5-1/2 wide x 8-1/2 long. I want to be able to print two to a page on a standard 8-1/2 X 11" piece of (nice quality) paper on a standard home printer.
Copy:
Made in Chicago Baby Shower
For: Marla & Gordon
Date: Saturday, April 5, 2014
Time: 7:00 p.m.
Place: 27 West Halbrook Ave, 4B
RSVP by April 1 to Nadia Verholm/312-555-0193

Hello Designers - I corrected the size requirements of the invitation (bad math before) and added a few more notes of preference. Looking for a design that is more clean and graphic and less traditional, soft baby shower look. Thank you!

Friends & family of the 20-sometthing, urban professional couple who are having a baby.

Baby

Must have
• Chicago flag colors and/or image, the words "made in Chicago", and the (revised) size indicated.
Should not have
• Anything inappropriate or offensive to grandmother of said couple.

```html
<!DOCTYPE html>
<html lang="en">
<head>
<meta charset="utf-8">
<title>Made in Chicago Baby Shower Invitation</title>
<link rel="stylesheet" href="https://fonts.googleapis.com/css2?family=Delius&family=Kalam:wght@700&family=Oswald:wght@700&display=swap">
<style>
  :root {
    --backdrop: #000000;
    --paper: #ffffff;
    --flag-blue: #b7def0;
    --flag-red: #ee1d23;
  }
  * { margin: 0; padding: 0; box-sizing: border-box; }
  html, body {
    width: 1200px;
    height: 998px;
    overflow: hidden;
    background: var(--backdrop);
  }
  .invitation {
    position: absolute;
    left: 348px;
    top: 116px;
    width: 503px;
    height: 766px;
    background: var(--paper);
    overflow: hidden;
  }
  .header-wave {
    position: absolute;
    left: 0;
    top: 0;
    width: 503px;
    height: 140px;
  }
  .headline {
    position: absolute;
    left: 0;
    top: 0;
    width: 503px;
    height: 140px;
    font-family: "Delius", "Comic Neue", sans-serif;
    font-weight: 400;
    color: var(--flag-red);
    font-size: 60px;
    line-height: 1;
  }
  .headline-baby {
    position: absolute;
    left: 28px;
    top: 22px;
  }
  .headline-shower {
    position: absolute;
    left: 212px;
    top: 50px;
    letter-spacing: -0.5px;
  }
  .details {
    position: absolute;
    left: 0;
    top: 164px;
    width: 490px;
    list-style: none;
    text-align: center;
    font-family: "Kalam", cursive;
    font-weight: 700;
    font-size: 25px;
    line-height: 54.5px;
    color: var(--flag-red);
  }
  .flag {
    position: absolute;
    left: 0;
    top: 501px;
    width: 503px;
    height: 230px;
  }
  .flag-band {
    position: absolute;
    left: 0;
    width: 100%;
    height: 76px;
    background: var(--flag-blue);
  }
  .flag-band--top { top: 0; }
  .flag-band--bottom { top: 153px; }
  .flag-stars {
    position: absolute;
    left: 0;
    top: 76px;
    width: 503px;
    height: 77px;
  }
  .tagline {
    position: absolute;
    left: 0;
    bottom: -2px;
    width: 503px;
    text-align: center;
    font-family: "Oswald", "Arial Narrow", sans-serif;
    font-weight: 700;
    font-size: 28px;
    line-height: 36px;
    color: var(--flag-red);
    transform: scaleX(0.9);
  }
</style>
</head>
<body>
  <main class="invitation">
    <svg class="header-wave" viewBox="0 0 503 140" aria-hidden="true">
      <path fill="var(--flag-blue)" d="M0,26 C140,-4 300,40 420,8 C460,-1 490,0 503,3 L503,100 C420,88 330,112 230,124 C130,136 50,134 0,128 Z"/>
    </svg>
    <h1 class="headline">
      <span class="headline-baby">Baby</span>
      <span class="headline-shower">Shower</span>
    </h1>

    <ul class="details">
      <li>For Marla &amp; Gordon</li>
      <li>on Saturday, April 5, 2014</li>
      <li>7.00 p.m. onwards</li>
      <li>at 27 West Halbrook Ave. 4B</li>
      <li>RSVP by April 1 to Nadia Verholm</li>
      <li>312-555-0193</li>
    </ul>

    <div class="flag">
      <div class="flag-band flag-band--top"></div>
      <svg class="flag-stars" viewBox="0 0 503 77" aria-hidden="true">
        <defs>
          <polygon id="six-point-star" points="0,-30 7.5,-13 26,-15 15,0 26,15 7.5,13 0,30 -7.5,13 -26,15 -15,0 -26,-15 -7.5,-13"/>
        </defs>
        <g fill="var(--flag-red)">
          <use href="#six-point-star" x="87" y="39"/>
          <use href="#six-point-star" x="192" y="39"/>
          <use href="#six-point-star" x="297" y="39"/>
          <use href="#six-point-star" x="402" y="39"/>
        </g>
      </svg>
      <div class="flag-band flag-band--bottom"></div>
    </div>

    <p class="tagline">MADE IN CHICAGO</p>
  </main>
</body>
</html>
```